Winter Fence Sale Fence Types

Please create a flyer, similar to what we did previous, but mimicking this page listing the fence styles: http://bramblewoodrails.com/snowfall-deal-2019

Industry/Entity Type

Residential Construction

Font styles to use
Sans Serif

Colors
cee9f5
33a6d7
d0dfed

Requirements
Must have
• Fence styles and photo of fence styles
Nice to have
• Phone number, address, logo

```html
<!DOCTYPE html>
<html lang="en">
<head>
<meta charset="utf-8">
<title>Bramblewood Rails – Winter Fence Sale</title>
<link rel="stylesheet" href="https://fonts.googleapis.com/css2?family=Anton&family=Fjalla+One&family=Barlow+Semi+Condensed:wght@600;700&display=swap">
<style>
  :root {
    --brand-blue: #3b6fb6;
    --title-blue: #3a82c8;
    --band-blue: rgba(59, 111, 182, 0.82);
    --amber: #d08a2e;
    --gold: #c8902f;
    --gold-dark: #b07a22;
    --bark: #45291e;
    --ink: #1d1d1d;
    --white: #ffffff;
    --sky: #cee9f5;
  }
  html, body {
    margin: 0;
    padding: 0;
    width: 862px;
    height: 1200px;
    overflow: hidden;
    background: var(--white);
  }
  .flyer {
    position: relative;
    width: 862px;
    height: 1200px;
    overflow: hidden;
    background: var(--white);
    font-family: "Barlow Semi Condensed", sans-serif;
  }

  /* Brand lockup */
  .brand { position: absolute; left: 42px; top: 14px; }
  .brand-square {
    position: absolute; left: 0; top: 4px;
    width: 84px; height: 84px;
    background: var(--bark);
  }
  .brand-name {
    position: absolute; left: 108px; top: 0;
    margin: 0;
    font-weight: 700; font-size: 33px; line-height: 40px;
    color: var(--title-blue);
    white-space: nowrap;
  }
  .brand-phone {
    position: absolute; left: 108px; top: 38px;
    font-weight: 700; font-size: 34px; line-height: 42px;
    color: var(--ink);
    white-space: nowrap;
  }
  .brand-tagline {
    position: absolute; left: 108px; top: 83px;
    font-weight: 700; font-size: 12px;
    color: var(--ink);
    white-space: nowrap;
  }

  /* Price banner */
  .price-banner { position: absolute; left: 0; top: 131px; width: 466px; height: 130px; }
  .price-banner svg { position: absolute; inset: 0; }
  .price-line, .price-value {
    position: absolute; margin: 0;
    font-family: "Fjalla One", sans-serif;
    color: var(--white);
    white-space: nowrap;
  }
  .price-line { left: 10px; top: 6px; font-size: 39px; line-height: 48px; letter-spacing: 0.5px; }
  .price-value { left: 72px; top: 50px; font-size: 62px; line-height: 76px; }

  /* Sale headline */
  .sale-title { position: absolute; left: 560px; top: 6px; width: 268px; height: 256px; }

  /* Fence style rows */
  .styles { position: absolute; left: 27px; top: 272px; width: 804px; }
  .style-row {
    position: relative;
    background: var(--brand-blue);
    padding: 4px;
    height: 156px;
    margin-bottom: 6px;
    box-sizing: content-box;
  }
  .style-photos {
    display: grid;
    grid-template-columns: repeat(3, 1fr);
    gap: 6px;
    height: 156px;
  }
  .style-photo { height: 156px; }
  .style-name {
    position: absolute; left: 4px; right: 4px; top: 4px;
    height: 30px; margin: 0;
    background: var(--band-blue);
    color: var(--white);
    font-family: "Barlow Semi Condensed", sans-serif;
    font-weight: 700; font-size: 27px; line-height: 30px;
    letter-spacing: 6px;
    text-align: center;
  }
  .wood-a { background: linear-gradient(160deg, #8fae6a 0%, #d9bf8c 45%, #c9a66e 100%); }
  .wood-b { background: linear-gradient(180deg, #6f8f4a 0%, #d8c08e 50%, #7f9a4e 100%); }
  .wood-c { background: linear-gradient(180deg, #5d7c43 0%, #d6b880 55%, #86a458 100%); }
  .metal-a { background: linear-gradient(180deg, #7d9a5a 0%, #3e4a36 55%, #8aa464 100%); }
  .metal-b { background: linear-gradient(180deg, #4f6a3c 0%, #4a4a44 55%, #9a8a6c 100%); }
  .metal-c { background: linear-gradient(180deg, #8fb060 0%, #3c4632 55%, #92a866 100%); }

  /* Illustration */
  .fence-illustration {
    position: absolute; left: 10px; top: 770px;
    width: 516px; height: 390px;
    background: radial-gradient(ellipse at 50% 50%, #d8a56c 0%, #c68d52 55%, rgba(255,255,255,0) 78%);
  }

  /* Showroom badge */
  .showroom {
    position: absolute; left: 543px; top: 748px;
    width: 294px; height: 294px; border-radius: 50%;
    background: radial-gradient(circle at 40% 35%, #d6a142 0%, var(--gold) 55%, var(--gold-dark) 100%);
    color: var(--white);
    font-family: "Fjalla One", sans-serif;
    text-align: center;
  }
  .showroom p { margin: 0; white-space: nowrap; }
  .showroom-invite { position: absolute; left: 0; right: 0; top: 58px; font-size: 27px; line-height: 38px; }
  .showroom-open { position: absolute; left: 0; right: 0; top: 170px; font-size: 40px; line-height: 46px; }
  .showroom-hours { position: absolute; left: 0; right: 0; top: 210px; font-size: 64px; line-height: 76px; }

  /* Footer: contact band and note */
  .footer-art { position: absolute; left: 0; top: 0; width: 862px; height: 1200px; }
  .contact-text {
    font-family: "Barlow Semi Condensed", sans-serif;
    font-weight: 700;
    fill: var(--white);
  }
  .styles-note {
    font-family: "Barlow Semi Condensed", sans-serif;
    font-weight: 600;
    fill: var(--brand-blue);
  }
</style>
</head>
<body>
<main class="flyer">

  <header class="brand">
    <span class="brand-square" aria-hidden="true"></span>
    <h1 class="brand-name">Bramblewood Rails</h1>
    <div class="brand-phone">704-555-0148</div>
    <div class="brand-tagline">“Because Good Fences Make Good Neighbors”</div>
  </header>

  <section class="price-banner">
    <svg width="466" height="130" viewBox="0 0 466 130" aria-hidden="true">
      <path d="M0 0 H466 C440 60 420 130 350 130 H0 Z" fill="var(--brand-blue)"/>
    </svg>
    <p class="price-line">WOOD FENCES STARTING</p>
    <p class="price-value">@ $12/FT</p>
  </section>

  <svg class="sale-title" viewBox="0 0 268 256" aria-label="Winter Fence Sale">
    <defs>
      <linearGradient id="saleSplit" gradientUnits="userSpaceOnUse" x1="150" y1="20" x2="200" y2="10">
        <stop offset="0.5" stop-color="var(--title-blue)"/>
        <stop offset="0.5" stop-color="var(--amber)"/>
      </linearGradient>
    </defs>
    <g font-family="Anton, sans-serif" fill="url(#saleSplit)" text-anchor="end">
      <text x="264" y="80" font-size="104" textLength="262" lengthAdjust="spacingAndGlyphs">WINTER</text>
      <text x="264" y="165" font-size="104" textLength="204" lengthAdjust="spacingAndGlyphs">FENCE</text>
      <text x="264" y="251" font-size="104" textLength="166" lengthAdjust="spacingAndGlyphs">SALE</text>
    </g>
  </svg>

  <section class="styles">
    <article class="style-row">
      <div class="style-photos">
        <div class="style-photo wood-a" role="img" aria-label="Photo of a tall pine privacy fence along a side yard"></div>
        <div class="style-photo wood-b" role="img" aria-label="Photo of a new privacy fence behind a rose bed"></div>
        <div class="style-photo wood-c" role="img" aria-label="Photo of a privacy fence with a palm tree in the yard"></div>
      </div>
      <h2 class="style-name">PRIVACY WOOD FENCE</h2>
    </article>
    <article class="style-row">
      <div class="style-photos">
        <div class="style-photo wood-b" role="img" aria-label="Photo of a scalloped picket fence around a backyard playset"></div>
        <div class="style-photo wood-a" role="img" aria-label="Photo of a scalloped picket fence corner"></div>
        <div class="style-photo wood-c" role="img" aria-label="Photo of a split-rail fence with an arched wooden gate"></div>
      </div>
      <h2 class="style-name">PICKET WOOD FENCE</h2>
    </article>
    <article class="style-row">
      <div class="style-photos">
        <div class="style-photo metal-a" role="img" aria-label="Photo of a black aluminium fence corner on a lawn"></div>
        <div class="style-photo metal-b" role="img" aria-label="Photo of an arched black aluminium double gate"></div>
        <div class="style-photo metal-c" role="img" aria-label="Photo of a black aluminium fence with spear tops"></div>
      </div>
      <h2 class="style-name">ALUMINIUM FENCE</h2>
    </article>
  </section>

  <div class="fence-illustration" role="img" aria-label="Illustration of a wooden picket fence section with capped posts"></div>

  <section class="showroom">
    <p class="showroom-invite">COME VISIT OUR<br>OUTDOOR<br>SHOWROOM</p>
    <p class="showroom-open">OPEN</p>
    <p class="showroom-hours">24/7!</p>
  </section>

  <svg class="footer-art" viewBox="0 0 862 1200" aria-label="Contact details">
    <path d="M862 1042 H470 C420 1042 385 1068 360 1105 L302 1200 H862 Z" fill="var(--brand-blue)"/>

    <!-- phone -->
    <g transform="translate(458 1047)">
      <circle cx="20" cy="20" r="20" fill="var(--white)"/>
      <path d="M13 11 L17 11 L19 16 L16.5 18 C18 21 19.5 22.5 22 24 L24 21.5 L29 23.5 L29 27.5 C29 28.5 28 29 27 29 C19 28.5 11.5 21 11 13 C11 12 12 11 13 11 Z" fill="none" stroke="var(--brand-blue)" stroke-width="1.8" stroke-linejoin="round"/>
    </g>
    <text class="contact-text" x="510" y="1083" font-size="42" textLength="332" lengthAdjust="spacingAndGlyphs">+1 704-555-0148</text>

    <!-- web -->
    <g transform="translate(396 1093)">
      <circle cx="20" cy="20" r="20" fill="var(--white)"/>
      <g fill="none" stroke="var(--brand-blue)" stroke-width="1.8">
        <circle cx="20" cy="20" r="11"/>
        <ellipse cx="20" cy="20" rx="5" ry="11"/>
        <path d="M9 20 H31 M11 14 H29 M11 26 H29"/>
      </g>
    </g>
    <text class="contact-text" x="456" y="1125" font-size="31" textLength="386" lengthAdjust="spacingAndGlyphs">bramblewoodrails.com</text>

    <!-- address -->
    <g transform="translate(340 1140)">
      <circle cx="20" cy="20" r="20" fill="var(--white)"/>
      <path d="M20 32 C15 25 12 21 12 17 A8 8 0 0 1 28 17 C28 21 25 25 20 32 Z" fill="var(--brand-blue)"/>
      <circle cx="20" cy="17" r="3.2" fill="var(--white)"/>
    </g>
    <text class="contact-text" x="396" y="1171" font-size="31" textLength="446" lengthAdjust="spacingAndGlyphs">417 Orchard Ln, Maple Grove, NC 28099</text>

    <text class="styles-note" x="76" y="1187" font-size="20" textLength="222" lengthAdjust="spacingAndGlyphs">Many Fence Styles Available</text>
  </svg>

</main>
</body>
</html>
```